Buch-/E-Book-Cover
Tolle Designerin. Tolles Ergebnis. Das beste war die reibungslose Kommunikation.
Zielgruppe
Wir verkaufen Trainings und vermitteln über unser Buch ein erstes vertieftes Wissen zum Thema Vermögensaufbau.
Aufgabenstellung
Es soll schlicht und schön sein, Angelehnt an Kluge Kinder arme Eltern, bzw. an Plane klug und werde frei von Bertram Quist.
Wir benötigen die AI, etc Dateien und die fertigen Dateien für Lesewelt.de Lumo sowie Lesewelt.de Books (ehemals Printfeld) mit fertigem Cover.
Vorgaben von Lesewelt.de über die Homepage. Anbei ein Beispiel (wegen Lesewelt.de Buchnummer etc) Abstände, Buchrücken etc.
Buch ca. 150 Seiten
https://www.lesewelt-beispiel.de/Gaertner-bleiben-ehrlich-Sommer-ruhigen/dp/7302958816 Front und Backcover kann man sich da ansehen.
Der Buchtitel ist 'Baue Mauern und bleibe frei' - - Lassen Sie uns freundschaftlich in entspannter Atmosphäre über Immobilien sprechen (der nebentitel so klein wie bei Kluge Kinder - Arme Eltern)
Rücktitel: Bitte zuerst Platzhalter.
Ich bitte um 5x8 inch, also wie DIN A 5, wir nehmen cremefarbenes Papier denke ich. Die Seitenzahl kann ich auf die Seite noch nicht sagen, wir haben aber 75 Din A4 Seiten, sprich nach Formatierung eher 160-165 Din A5. WErde ich Ihnen final nach dem Gewinn sagen.
Versuchen Sie mich mal aus dem einen Bild raus zu schneiden, und dass dann mit einem Layer über das cover zu legen.
2-3 Versionen wäre gut, mit 2-3 Bildern. Buchrücken ein kleines Bild von mir.
Seite vom Buch: Titel nochmal.

```html
<!DOCTYPE html>
<html lang="de">
<head>
<meta charset="utf-8">
<title>Baue Mauern und bleibe frei – Covervarianten</title>
<link rel="stylesheet" href="https://fonts.googleapis.com/css2?family=Lato:wght@400;700;900&display=swap">
<style>
  :root {
    --page: #ffffff;
    --plum-dark: #1f0a1c;
    --plum: #3b1233;
    --plum-light: #521a47;
    --magenta: #c0187e;
    --magenta-deep: #6e0f4c;
    --gold: #f6b52a;
    --white: #ffffff;
    --banner: #2b1838;
    --badge: #2e1a3c;
    --photo-dark: #3a2a26;
    --photo-light: #8b7266;
  }
  * { margin: 0; padding: 0; box-sizing: border-box; }
  html, body {
    width: 1200px; height: 3000px; overflow: hidden;
    background: var(--page);
    font-family: "Lato", Arial, sans-serif;
  }
  .cover {
    position: absolute; overflow: hidden;
    background: linear-gradient(160deg, var(--plum-light) 0%, var(--plum) 45%, var(--plum-dark) 100%);
  }
  .cover--a { left: 258px; top: 240px; width: 752px; height: 1168px; }
  .cover--b { left: 266px; top: 1590px; width: 736px; height: 1170px; }
  .cover__stripes { position: absolute; inset: 0; width: 100%; height: 100%; }
  .cover__portrait {
    position: absolute; bottom: 0;
    background: linear-gradient(180deg, var(--photo-light) 0%, var(--photo-dark) 60%, #2a1e1c 100%);
    border-radius: 120px 120px 0 0;
    opacity: .9;
  }
  .cover--a .cover__portrait { left: 400px; top: 60px; width: 340px; }
  .cover--b .cover__portrait { left: 474px; top: 20px; width: 262px; }
  .author { position: absolute; color: var(--white); font-size: 26px; line-height: 34px; }
  .author__name { font-weight: 900; }
  .cover--a .author { left: 0; right: 0; top: 34px; text-align: center; }
  .cover--b .author { left: 68px; top: 34px; }
  .cover--b .author__name { color: var(--gold); display: block; }
  .title {
    position: absolute; text-align: center; font-weight: 900;
    text-transform: uppercase; line-height: .98;
    text-shadow: 0 4px 18px rgba(0,0,0,.35);
  }
  .cover--a .title { left: 82px; width: 600px; top: 462px; }
  .cover--b .title { left: 74px; width: 600px; top: 522px; }
  .title__gold { display: block; color: var(--gold); font-size: 98px; }
  .title__white { display: block; color: var(--white); font-size: 98px; }
  .title__link { display: block; color: var(--white); font-size: 36px; font-weight: 700; text-transform: none; margin: 4px 0 2px 150px; }
  .subtitle-bar {
    position: absolute; background: var(--banner);
    color: var(--gold); font-weight: 700; font-size: 34px;
    text-align: center; line-height: 64px; text-transform: uppercase;
  }
  .cover--a .subtitle-bar { left: 70px; width: 628px; top: 960px; height: 64px; }
  .cover--b .subtitle-bar { left: 74px; width: 612px; top: 1010px; height: 64px; }
  .tagline {
    position: absolute; left: 0; width: 704px; top: 1058px;
    color: var(--white); font-size: 27px; line-height: 34px; text-align: center;
  }
  .badge {
    position: absolute; left: 56px; top: 326px; width: 208px; height: 208px;
    border-radius: 50%; background: var(--badge);
    color: var(--gold); font-weight: 700; font-size: 20px; line-height: 23px;
    display: flex; align-items: center; justify-content: center; text-align: center;
    padding: 0 22px;
  }
</style>
</head>
<body>

<section class="cover cover--a" aria-label="Covervariante 1">
  <svg class="cover__stripes" viewBox="0 0 752 1168" preserveAspectRatio="none" aria-hidden="true">
    <polygon points="0,1240 752,660 752,760 0,1340" fill="var(--magenta-deep)"/>
    <polygon points="0,1200 752,760 752,880 0,1330" fill="var(--magenta)" opacity=".85"/>
    <polygon points="0,1168 752,880 752,1168" fill="var(--plum-dark)" opacity=".7"/>
  </svg>
  <div class="cover__portrait" role="img" aria-label="Freigestelltes Porträtfoto des Autors im braunen Anzug"></div>
  <p class="author"><span class="author__name">DENIZ BRANDT –</span> DER IMMOBILIENADVISOR</p>
  <h1 class="title">
    <span class="title__gold">Baue</span>
    <span class="title__gold">Mauern</span>
    <span class="title__link">und</span>
    <span class="title__white">Bleibe</span>
    <span class="title__white">Frei</span>
  </h1>
  <p class="subtitle-bar">Gespräche über Immobilien</p>
  <p class="tagline" style="left:24px">Lassen Sie uns unter Freunden in entspannter<br>Atmosphäre über Immobilien sprechen</p>
</section>

<section class="cover cover--b" aria-label="Covervariante 2">
  <svg class="cover__stripes" viewBox="0 0 736 1170" preserveAspectRatio="none" aria-hidden="true">
    <polygon points="0,1200 736,660 736,760 0,1300" fill="var(--magenta-deep)"/>
    <polygon points="0,1170 736,780 736,900 0,1290" fill="var(--magenta)" opacity=".75"/>
    <polygon points="0,1170 736,900 736,1170" fill="var(--plum-dark)" opacity=".7"/>
  </svg>
  <div class="cover__portrait" role="img" aria-label="Freigestelltes Porträtfoto des Autors im braunen Anzug"></div>
  <p class="author"><span class="author__name">DENIZ BRANDT –</span>DER IMMOBILIENADVISOR</p>
  <p class="badge">Lassen Sie uns unter Freunden in entspannter Atmosphäre über Immobilien sprechen</p>
  <h1 class="title">
    <span class="title__gold">Baue</span>
    <span class="title__gold">Mauern</span>
    <span class="title__link">und</span>
    <span class="title__white">Bleibe</span>
    <span class="title__white">Frei</span>
  </h1>
  <p class="subtitle-bar">Gespräche über Immobilien</p>
</section>

</body>
</html>
```